Velbrook Leaf is a bridge for the people who drink tea to connect with the people who make the tea and the environment in which it is grown.

As a start-up, Velbrook Leaf needs to establish a fluently persuasive brand image that articulates its unique mission to the up-market tea drinker.

Our passion for high quality tea and our respect for people are boundless. But our budget is shoe-string. Still, we will allocate a disproportionate amount to evolving a brand; including logo, labeling, and packaging, and hope this initial effort will lead to a long-term relationship with a designer. The Velbrook label, as a component of the brand, must deny the commodity image of tea by broadcasting the uniquely flavorful, healthful, and relaxing experience of drinking tea.

The logo is an image of a liquor pouring from above into a stylized outline of a cup and gracefully folding over on itself within the cup. The image is an echo of video clips that will be featured on the Product page of the ecommerce site. Our initial thought is for the liquor and cup to be white on a rich blue background. But you may have a better idea.

The label must fit a seamless tin canister 4" in diameter; 2" high with a "window" in the lid. There are really three distinct parts to the label: a) wrap-around for the body of the tin; b) a distinct piece to be applied underneath the tin; and c) security strip (s) that connect the lid and the bottom of the tin. The wrap-around must include the following components: the logo, the brand name 'Velbrook Leaf', the name of the specific tea and space for the following characteristics of the tea: Tea / Garden Name, Harvest Date, Tasting Notes, Weight, Location, and Caffeine content. The piece to be affixed underneath the tin should accommodate Ingredients, Brewing Instructions, and contact details for Velbrook Leaf. The security strip(s) should be an integral part of the overall visual.

The color scheme should be expandable, i.e.; different colors for different teas.
We are thinking about rich and bold colors. But am eager to see what inspires you!

A very rough proto-type is captured in the attached files.

Target Market(s)

Ages 25 to 45 in densely populated areas of the U.S. and Canada will an above average house-hold income and an interest in what they eat / drink.

Industry/Entity Type

Environment

Requirements
Must have
• 1. Three separate pieces: 1) wrap around for the body of the tin; 2) piece to be affixed to the bottom of the body of the tin; 3) security strip (s). A word about strips: am unsure about one vs two because, two will add to overhead and processing while one will block the view of the contents. Maybe you know how to resolve.
2. clean, crisp lines
3. uncluttered
Nice to have
• 1. a color scheme to accommodate up to 30 different teas. Do not fall into the trap of incorporating the color green on the label for a 'green tea' and yellow for a lemon flavored tea. That approach is limited and has been overdone.
2. a color scheme that, as it expands to accommodate 30 teas, also is anchored by a brand color set. In other words, all labels include a recognizable color set.
3. express the level of caffeine via a gauge or metric
Should not have
• photo images,

```html
<!DOCTYPE html>
<html lang="en">
<head>
<meta charset="utf-8">
<title>Velbrook Leaf — Tin Label Concepts</title>
<link rel="stylesheet" href="https://fonts.googleapis.com/css2?family=Cormorant+Garamond:ital,wght@1,500;1,600&family=Oranienbaum&display=swap">
<style>
  :root {
    --royal-blue: #2b3990;
    --navy: #0b2a62;
    --paper: #ffffff;
    --frame-grey: #d6d6d6;
    --sky-cup: #3fa2dc;
    --tea-brown: #a97c50;
    --shadow: rgba(0, 0, 0, 0.45);
  }
  html, body {
    margin: 0;
    padding: 0;
    width: 835px;
    height: 1200px;
    overflow: hidden;
    background: var(--paper);
  }
  .label-sheet {
    display: block;
    width: 835px;
    height: 1200px;
  }
  .script-type {
    font-family: "Cormorant Garamond", "Times New Roman", serif;
    font-style: italic;
    font-weight: 600;
  }
  .condensed-type {
    font-family: "Oranienbaum", "Times New Roman", serif;
  }
  .brand-title { fill: var(--paper); }
  .royal-ink { fill: var(--royal-blue); }
  .navy-ink { fill: var(--navy); }
  .label-frame { fill: none; stroke: var(--frame-grey); stroke-width: 1; }
</style>
</head>
<body>
<svg class="label-sheet" viewBox="0 0 620 902" preserveAspectRatio="xMidYMid meet" xmlns="http://www.w3.org/2000/svg">
  <defs>
    <filter id="badge-shadow" x="-30%" y="-30%" width="160%" height="160%">
      <feDropShadow dx="2" dy="3" stdDeviation="3" flood-color="#000" flood-opacity="0.45"/>
    </filter>
    <radialGradient id="cup-tones" cx="50%" cy="55%" r="60%">
      <stop offset="0%" stop-color="#8fd0f2"/>
      <stop offset="55%" stop-color="#3fa2dc"/>
      <stop offset="100%" stop-color="#2b3990"/>
    </radialGradient>
    <radialGradient id="steam-cup-tones" cx="50%" cy="55%" r="60%">
      <stop offset="0%" stop-color="#f2ebe2"/>
      <stop offset="60%" stop-color="#c9a27a"/>
      <stop offset="100%" stop-color="#a97c50"/>
    </radialGradient>
  </defs>

  <!-- Concept A: royal blue -->
  <g class="concept concept-royal">
    <rect class="security-strip" x="289" y="18" width="40" height="180" fill="var(--royal-blue)"/>
    <rect class="label-frame" x="24" y="197" width="571" height="214"/>
    <rect class="header-band" x="24" y="197" width="571" height="82" fill="var(--royal-blue)"/>
    <text class="brand-title script-type" x="309" y="227" text-anchor="middle" font-size="30">Velbrook Leaf</text>

    <g class="caffeine-gauge">
      <text class="royal-ink script-type" font-size="11" text-anchor="middle" transform="translate(100 340) rotate(-90)">Caffeine Level</text>
      <rect x="111" y="287" width="15" height="15" transform="rotate(45 118.5 294.5)" fill="var(--royal-blue)"/>
      <rect x="111" y="311" width="15" height="15" transform="rotate(45 118.5 318.5)" fill="var(--royal-blue)"/>
      <rect x="111" y="335" width="15" height="15" transform="rotate(45 118.5 342.5)" fill="var(--royal-blue)"/>
      <rect x="111" y="359" width="15" height="15" transform="rotate(45 118.5 366.5)" fill="var(--royal-blue)"/>
      <rect x="111" y="383" width="15" height="15" transform="rotate(45 118.5 390.5)" fill="var(--royal-blue)"/>
    </g>

    <g class="emblem-badge">
      <rect x="259" y="257" width="100" height="100" transform="rotate(45 309 307)" fill="var(--paper)" filter="url(#badge-shadow)"/>
      <rect x="267" y="265" width="84" height="84" transform="rotate(45 309 307)" fill="url(#cup-tones)" role="img" aria-label="Illustration of a steaming light-blue teacup on a saucer"/>
    </g>
    <text class="royal-ink script-type" x="309" y="401" text-anchor="middle" font-size="19">name of tea</text>

    <g class="tea-details royal-ink script-type" font-size="12">
      <text x="392" y="297">Harvest Date</text>
      <text x="392" y="331">Tasting Notes</text>
      <text x="392" y="365">Weight</text>
      <text x="392" y="399">Growing Region</text>
    </g>
  </g>

  <!-- Concept B: navy wave -->
  <g class="concept concept-navy">
    <rect class="security-strip" x="289" y="494" width="40" height="180" fill="var(--navy)"/>
    <rect class="label-frame" x="24" y="673" width="571" height="213"/>
    <path class="header-wave" d="M24,673 H595 V755 C530,785 465,803 405,801 C300,797 160,728 24,752 Z" fill="var(--navy)"/>
    <text class="brand-title condensed-type" x="309" y="703" text-anchor="middle" font-size="24">Velbrook Leaf</text>

    <g class="emblem-badge">
      <rect x="261" y="742" width="96" height="96" transform="rotate(45 309 790)" fill="var(--paper)" filter="url(#badge-shadow)"/>
      <rect x="266" y="747" width="86" height="86" transform="rotate(45 309 790)" fill="none" stroke="var(--navy)" stroke-width="1"/>
      <rect x="283" y="735" width="52" height="88" rx="6" fill="url(#steam-cup-tones)" role="img" aria-label="Illustration of a steaming cup of tea on a white saucer"/>
    </g>
    <text class="navy-ink condensed-type" x="309" y="880" text-anchor="middle" font-size="17">name of tea</text>

    <g class="tea-details navy-ink condensed-type" font-size="10">
      <text x="37" y="769">Harvest Date</text>
      <text x="37" y="803">Tasting Notes</text>
      <text x="37" y="837">Weight</text>
      <text x="37" y="871">Growing Region</text>
    </g>

    <g class="caffeine-gauge">
      <text class="navy-ink condensed-type" x="530" y="849" text-anchor="middle" font-size="10">Caffeine Level</text>
      <g fill="none" stroke="var(--navy)" stroke-width="1.2">
        <rect x="473" y="862" width="14" height="14" transform="rotate(45 480 869)"/>
        <rect x="496" y="862" width="14" height="14" transform="rotate(45 503 869)"/>
        <rect x="519" y="862" width="14" height="14" transform="rotate(45 526 869)"/>
        <rect x="542" y="862" width="14" height="14" transform="rotate(45 549 869)"/>
        <rect x="565" y="862" width="14" height="14" transform="rotate(45 572 869)"/>
      </g>
    </g>
  </g>
</svg>
</body>
</html>
```